BRAVEK THERAPEUTICS

physical therapy company. need a flashy image and named logo, website link, that I can also use on Letterhead and business cards. Clean, sharp, modern, eye catching. 3 colors? Some shine. Needs to stand out and not be trendy or too much cursive . Androgynous image of a human body is ok. A spine included is ok. Prefer lines to curves for font types. Warm colors but strong impact. Will need to have some contact info and border mission statement on it.

Target Market(s)

Target market is large corporations, wealthy individuals, medical doctors

Industry/Entity Type

Medical, physical therapy

Contact Information for Business Card

Name, Owner, phone, email, and website

Colors
0054AA
0677BA
7BADD7
CADEEF
E8F1F8

Requirements
Must have
• See above- something about BALANCE, wellness, strength etc
Nice to have
• Contrast, depth
Should not have
• No cursive

```html
<!DOCTYPE html>
<html lang="en">
<head>
<meta charset="utf-8">
<title>Bravek Therapeutics – Business Card</title>
<link rel="stylesheet" href="https://fonts.googleapis.com/css2?family=Montserrat:wght@300;400;500&display=swap">
<style>
  :root {
    --bg: #2b2b2b;
    --royal: #0054AA;
    --sky: #7BADD7;
    --mist: #CADEEF;
    --ice: #E8F1F8;
    --white: #ffffff;
    --silver-light: #d4d4d4;
    --silver-dark: #9c9c9c;
  }
  * { box-sizing: border-box; margin: 0; padding: 0; }
  html, body { width: 1200px; height: 866px; overflow: hidden; }
  body {
    background: var(--bg);
    font-family: "Montserrat", sans-serif;
    color: var(--white);
    display: flex;
    flex-direction: column;
    align-items: center;
    justify-content: center;
    gap: 40px;
  }
  .card {
    position: relative;
    width: 640px;
    height: 366px;
    background: var(--royal);
    overflow: hidden;
    box-shadow: 0 10px 24px rgba(0,0,0,0.55);
  }
  .wordmark {
    position: absolute;
    font-weight: 400;
    letter-spacing: 0.04em;
    white-space: nowrap;
    color: var(--white);
  }

  /* Front */
  .contact { position: absolute; left: 38px; top: 40px; }
  .contact__name { font-size: 17px; font-weight: 500; letter-spacing: 0.08em; text-transform: uppercase; }
  .contact__role { font-size: 14px; font-weight: 400; letter-spacing: 0.06em; margin-bottom: 12px; }
  .contact__row { display: flex; align-items: center; gap: 8px; font-size: 14px; font-weight: 400; letter-spacing: 0.04em; line-height: 1.45; }
  .contact__row svg { width: 14px; height: 14px; flex: none; }
  .card--front .wordmark { left: 300px; top: 150px; font-size: 25px; }
  .rule { position: absolute; left: 200px; right: 40px; top: 210px; height: 1px; background: var(--sky); opacity: 0.8; }
  .footer-band { position: absolute; left: 0; bottom: 0; width: 640px; height: 60px; }
  .website {
    position: absolute; right: 34px; bottom: 9px;
    font-size: 14px; letter-spacing: 0.08em; color: var(--white);
  }

  /* Back */
  .figure-area {
    position: absolute; left: 0; top: 0; width: 240px; height: 366px;
    background: linear-gradient(160deg, var(--silver-light) 0%, var(--silver-dark) 100%);
  }
  .card--back .wordmark { left: 268px; top: 160px; font-size: 27px; }
</style>
</head>
<body>

  <section class="card card--front">
    <div class="contact">
      <p class="contact__name">Marcus Hale</p>
      <p class="contact__role">Managing Director</p>
      <p class="contact__row">
        <svg viewBox="0 0 16 16" aria-hidden="true"><path d="M4 1.5l2.5 3-1.5 1.6c.8 1.8 2.1 3.1 3.9 3.9L10.5 8.5l3 2.5-1.3 2.6C7 13.3 2.7 9 2.4 3.8z" fill="var(--white)"/></svg>
        044-555 210 384
      </p>
      <p class="contact__row">
        <svg viewBox="0 0 16 16" aria-hidden="true"><rect x="1" y="3.5" width="14" height="9" fill="var(--white)"/><path d="M1 3.5l7 5 7-5" fill="none" stroke="var(--royal)" stroke-width="1.2"/></svg>
        info@bravekthera.com
      </p>
    </div>

    <p class="wordmark">BRAVEK THERAPEUTICS</p>
    <div class="rule"></div>

    <svg class="footer-band" viewBox="0 0 640 60" aria-hidden="true">
      <path d="M0 24 L238 24 C256 24 262 6 290 6 L640 6 L640 60 L0 60 Z" fill="var(--sky)"/>
      <path d="M0 32 L240 32" stroke="var(--mist)" stroke-width="4"/>
      <path d="M0 40 L240 40 L240 60 L0 60 Z" fill="var(--royal)"/>
    </svg>
    <p class="website">www.bravektherapeutics.com</p>
  </section>

  <section class="card card--back">
    <div class="figure-area" role="img" aria-label="Silver rendered human figure seen from the side, spine visible, sitting in a forward stretch"></div>
    <p class="wordmark">BRAVEK THERAPEUTICS</p>
  </section>

</body>
</html>
```